Telecom ISP Business Cards and Stationary
Wireless Internet Service Provider
Telecom ISP Business Cards and Stationary - Telecommunications
Creative Brief
Bright & Fun-filled
Leopold Hartvig
Network Manager
4176 Coralwood Ridge Rd. Ste 240 Henderson, NV 89114
leopold@skylornnet.example
www.skylornnet.example

```html
<!DOCTYPE html>
<html lang="en">
<head>
<meta charset="UTF-8">
<title>Skylorn Net Business Card</title>
<link href="https://fonts.googleapis.com/css2?family=Exo+2:wght@400;600;800&display=swap" rel="stylesheet">
<style>
  :root {
    --bg: #8d8d8d;
    --card: #ffffff;
    --navy: #232a5c;
    --lime: #a6c83a;
    --grey: #6d6e73;
    --ink: #2b2d3a;
    --rule: #d4d6dc;
  }
  * { margin: 0; padding: 0; box-sizing: border-box; }
  html, body { width: 1200px; height: 908px; overflow: hidden; }
  body {
    background: var(--bg);
    font-family: "Exo 2", sans-serif;
    display: flex;
    align-items: center;
    justify-content: center;
    gap: 60px;
  }
  .card {
    width: 500px;
    height: 286px;
    background: var(--card);
    border-radius: 14px;
    position: relative;
    overflow: hidden;
    box-shadow: 0 6px 18px rgba(0,0,0,.25);
  }
  /* Front */
  .card-front { display: flex; align-items: center; justify-content: center; }
  .brand { display: flex; align-items: center; gap: 10px; }
  .brand-dot { width: 18px; height: 18px; border-radius: 50%; background: var(--lime); }
  .brand-name {
    font-weight: 800;
    color: var(--navy);
    text-transform: uppercase;
    letter-spacing: 1px;
  }
  .card-front .brand-name { font-size: 38px; }
  /* Back */
  .card-back .brand { position: absolute; left: 30px; top: 62px; }
  .card-back .brand-name { font-size: 30px; }
  .card-back .brand-dot { width: 14px; height: 14px; }
  .person { position: absolute; left: 30px; bottom: 70px; }
  .person-name { font-size: 20px; color: var(--ink); font-weight: 400; }
  .person-role { font-size: 12px; color: var(--lime); font-weight: 600; margin-top: 2px; }
  .contact {
    position: absolute;
    left: 300px;
    top: 34px;
    bottom: 46px;
    padding-left: 16px;
    border-left: 1px solid var(--rule);
    font-size: 10.5px;
    color: var(--grey);
    display: flex;
    flex-direction: column;
    gap: 7px;
    justify-content: center;
  }
  .contact-address { line-height: 1.45; margin-bottom: 4px; }
  .contact-row { display: flex; align-items: center; gap: 6px; }
  .contact-row svg { flex: none; }
  .band-web {
    position: absolute;
    left: 0; right: 0; bottom: 14px;
    height: 24px;
    background: var(--lime);
    color: #fff;
    font-size: 11px;
    font-weight: 600;
    display: flex;
    align-items: center;
    justify-content: flex-end;
    padding-right: 24px;
    clip-path: polygon(290px 0, 100% 0, 100% 100%, 270px 100%);
  }
  .band-navy {
    position: absolute;
    left: 0; right: 0; bottom: 0;
    height: 14px;
    background: var(--navy);
  }
</style>
</head>
<body>
  <section class="card card-front">
    <div class="brand">
      <span class="brand-dot"></span>
      <span class="brand-name">Skylorn Net</span>
    </div>
  </section>

  <section class="card card-back">
    <div class="brand">
      <span class="brand-dot"></span>
      <span class="brand-name">Skylorn Net</span>
    </div>
    <div class="person">
      <div class="person-name">Leopold Hartvig</div>
      <div class="person-role">Network Manager</div>
    </div>
    <div class="contact">
      <div class="contact-address">4176 Coralwood Ridge Rd. Ste 240<br>Henderson, NV 89114</div>
      <div class="contact-row">
        <svg width="12" height="12" viewBox="0 0 12 12"><circle cx="6" cy="6" r="6" fill="var(--lime)"/><path d="M4 3.2l1 1.4-.6.7a4 4 0 0 0 2.3 2.3l.7-.6 1.4 1-.5 1A5.5 5.5 0 0 1 3 4z" fill="#fff"/></svg>
        <span>702-555-0148</span>
      </div>
      <div class="contact-row">
        <svg width="12" height="12" viewBox="0 0 12 12"><circle cx="6" cy="6" r="6" fill="var(--navy)"/><path d="M4 3.2l1 1.4-.6.7a4 4 0 0 0 2.3 2.3l.7-.6 1.4 1-.5 1A5.5 5.5 0 0 1 3 4z" fill="#fff"/></svg>
        <span>702-555-0193</span>
      </div>
      <div class="contact-row">
        <svg width="12" height="12" viewBox="0 0 12 12"><circle cx="6" cy="6" r="6" fill="var(--lime)"/><rect x="3" y="4" width="6" height="4.2" fill="none" stroke="#fff" stroke-width=".9"/><path d="M3 4l3 2.3L9 4" fill="none" stroke="#fff" stroke-width=".9"/></svg>
        <span>leopold@skylornnet.example</span>
      </div>
    </div>
    <div class="band-web">www.skylornnet.example</div>
    <div class="band-navy"></div>
  </section>
</body>
</html>
```